Ashcombe Prep Keystone Academy

I need a tri-fold brochure with attached information for an established private school (Ashcombe Preparatory School) based in Wellington, Florida (South Florida). We are beginning a new program (Ashcombe Prep 'Keystone' Academy) for students who are looking for a non-traditional approach to education (1 Student, 1 Teacher, Flexible Scheduling). Pictures can be altered.

Target Market(s)

Middle and High School age students and their parents

Industry/Entity Type

Education

Requirements
Must have
• Ashcombe Prep Logo...General attached information...Contact Info.

```html
<!DOCTYPE html>
<html lang="en">
<head>
<meta charset="utf-8">
<title>Ashcombe Keystone Academy – Tri-fold Brochure</title>
<link href="https://fonts.googleapis.com/css2?family=Arimo:ital,wght@0,400;0,700;1,700&family=Cormorant+Garamond:wght@500;600&display=swap" rel="stylesheet">
<style>
:root{
  --orange:#e8671f;
  --orange-light:#ef8448;
  --blue:#1d5fb0;
  --blue-dark:#163f86;
  --blue-title:#1f5aa6;
  --sky:#8cc3ef;
  --ink:#4a4a4a;
  --page:#e6e6e6;
  --white:#ffffff;
}
*{margin:0;padding:0;box-sizing:border-box}
html,body{width:1200px;height:1200px;overflow:hidden;background:var(--page);font-family:"Arimo",Arial,sans-serif}
.spread{position:absolute;left:204px;width:792px;height:560px;background:var(--white);box-shadow:0 2px 6px rgba(0,0,0,.15);overflow:hidden}
.spread--outside{top:20px}
.spread--inside{top:620px}
.spread svg.art{position:absolute;left:0;top:0;width:792px;height:560px}
.txt{position:absolute;color:var(--ink)}
.heading-italic{font-weight:700;font-style:italic;font-size:15px}
.academics-title{left:22px;top:238px;color:var(--blue)}
.academics-body{left:22px;top:262px;width:220px;font-size:7.6px;line-height:1.3;text-align:justify}
.bullets{list-style:none;font-size:7.6px}
.bullets li{height:18px;line-height:18px;padding-left:12px;position:relative}
.bullets li::before{content:"»";position:absolute;left:0;color:var(--orange);font-weight:700}
.academics-list{left:22px;top:368px;width:230px}
.endeavors-title{left:288px;top:178px;color:var(--white)}
.endeavors-body{left:288px;top:202px;width:218px;font-size:7.6px;line-height:1.3;color:var(--white);text-align:justify}
.endeavors-list{left:288px;top:307px;width:230px;color:var(--white)}
.endeavors-list li::before{color:var(--white)}
.endeavors-close{left:288px;top:436px;width:218px;font-size:7.6px;line-height:1.4;color:var(--white)}
.brand{left:528px;top:70px;width:264px;text-align:center;font-family:"Cormorant Garamond",serif;color:var(--blue-dark)}
.brand-name{font-size:17px;font-weight:600;letter-spacing:.5px}
.brand-sub{font-size:6px;letter-spacing:1px;margin-top:2px}
.cover-title{left:528px;top:426px;width:264px;text-align:center;font-family:"Cormorant Garamond",serif;font-weight:500;line-height:1}
.cover-title .line1{font-size:32px;color:var(--sky);letter-spacing:.5px}
.cover-title .line2{font-size:32px;color:var(--white);letter-spacing:1px}
.contact{font-size:7.4px;color:var(--white);line-height:1.6}
.cover-address{left:562px;top:514px}
.cover-phone{left:674px;top:514px}
.diff-title{left:200px;top:150px;width:392px;text-align:center;font-family:"Cormorant Garamond",serif;font-weight:600;font-size:27px;line-height:1.1;color:var(--blue-title)}
.col{top:250px;font-size:9.2px;line-height:1.32}
.col-1{left:44px;width:196px}
.col-2{left:310px;width:175px;text-align:justify}
.col-3{left:554px;width:185px}
.col p+p{margin-top:12px}
.footer-text{font-size:9.4px;color:var(--white);line-height:1.4}
.foot-name{left:32px;top:522px}
.foot-address{left:310px;top:514px}
.foot-contact{left:590px;top:514px}
</style>
</head>
<body>

<section class="spread spread--outside">
<svg class="art" viewBox="0 0 792 560" xmlns="http://www.w3.org/2000/svg">
  <defs>
    <linearGradient id="photoWarm" x1="0" y1="0" x2="1" y2="1">
      <stop offset="0" stop-color="#e3c09e"/><stop offset=".55" stop-color="#c58a74"/><stop offset="1" stop-color="#9fb59a"/>
    </linearGradient>
    <linearGradient id="photoGreen" x1="0" y1="0" x2="0" y2="1">
      <stop offset="0" stop-color="#7f9c55"/><stop offset="1" stop-color="#3e5a2b"/>
    </linearGradient>
    <linearGradient id="photoTeens" x1="0" y1="0" x2="1" y2="1">
      <stop offset="0" stop-color="#d8b397"/><stop offset=".5" stop-color="#b88c70"/><stop offset="1" stop-color="#8fb0c4"/>
    </linearGradient>
    <linearGradient id="fadeSky" x1="0" y1="0" x2="0" y2="1">
      <stop offset="0" stop-color="#bcd9f3"/><stop offset="1" stop-color="#ffffff"/>
    </linearGradient>
  </defs>
  <path role="img" aria-label="Photo: teacher and student working together at a desk" d="M0 0H264V140Q130 160 0 215Z" fill="url(#photoWarm)"/>
  <path d="M0 215Q130 160 264 140V152Q140 175 0 235Z" fill="var(--orange)"/>
  <path d="M0 235Q140 175 264 152V330H0Z" fill="url(#fadeSky)"/>
  <path role="img" aria-label="Photo: student riding a horse in an equestrian arena" d="M264 0H528V130Q400 125 264 148Z" fill="url(#photoGreen)"/>
  <path d="M264 148Q400 125 528 130V560H264Z" fill="var(--orange)"/>
  <rect x="264" y="325" width="264" height="18" fill="var(--orange-light)"/>
  <rect x="264" y="361" width="264" height="18" fill="var(--orange-light)"/>
  <rect x="264" y="397" width="264" height="18" fill="var(--orange-light)"/>
  <rect x="622" y="42" width="20" height="20" fill="var(--blue-dark)"/>
  <path role="img" aria-label="Photo: group of smiling middle and high school students" d="M528 150Q650 130 792 112V385Q660 400 528 420Z" fill="url(#photoTeens)"/>
  <path d="M528 420Q660 400 792 385V396Q660 412 528 434Z" fill="var(--orange)"/>
  <path d="M528 434Q660 412 792 396V560H528Z" fill="var(--blue)"/>
  <line x1="528" y1="505" x2="792" y2="505" stroke="#ffffff" stroke-opacity=".35" stroke-dasharray="2 2"/>
  <path d="M547 518a4 4 0 0 1 8 0c0 3-4 7-4 7s-4-4-4-7z" fill="var(--orange)"/>
  <circle cx="551" cy="518" r="1.4" fill="#fff"/>
  <circle cx="666" cy="520" r="4" fill="var(--orange)"/>
  <path d="M664 518l1 -1 1 2 -.7.7a3 3 0 0 0 1.5 1.5l.7-.7 2 1-1 1a4 4 0 0 1-4.5-4.5z" fill="#fff"/>
  <circle cx="666" cy="532" r="4" fill="var(--orange)"/>
  <circle cx="666" cy="532" r="2.2" fill="none" stroke="#fff" stroke-width=".7"/>
  <line x1="663.8" y1="532" x2="668.2" y2="532" stroke="#fff" stroke-width=".6"/>
</svg>

<h2 class="txt heading-italic academics-title">Academics</h2>
<p class="txt academics-body">The Ashcombe Keystone Academy offers top academics in a customized setting. Students are paired with a single teacher creating the 1:1 model, which is at the core of our offering. Teachers are able to accelerate or review course material, allowing students to meet once per week while progressing through subjects at a traditional schooling pace.</p>
<ul class="txt bullets academics-list">
  <li>Year Round Entry</li>
  <li>Flexible Scheduling</li>
  <li>Most students meet one hour / week per course</li>
  <li>Accredited Courses</li>
  <li>F1 Visas (SEVIS Certified) For International Students</li>
  <li>Boarding or Homestay</li>
</ul>

<h2 class="txt heading-italic endeavors-title">Student Endeavors</h2>
<p class="txt endeavors-body">Traditional schooling does not work for every student. At The Ashcombe Keystone Academy, we understand some students pursue other specialized endeavors and need a more customized academic experience. We can accommodate students irrespective of their schedule and also offer partnerships with a variety of athletic and fine arts academies including:</p>
<ul class="txt bullets endeavors-list">
  <li>Equestrian</li>
  <li>Tennis</li>
  <li>Ice Skating</li>
  <li>Basketball &amp; Baseball</li>
  <li>Golf</li>
  <li>Acting &amp; Music</li>
  <li>Many others</li>
</ul>
<p class="txt endeavors-close">Our flexible program will provide the perfect fit for your schedule.</p>

<div class="txt brand">
  <div class="brand-name">ASHCOMBE</div>
  <div class="brand-sub">PREPARATORY SCHOOL</div>
</div>
<h1 class="txt cover-title"><span class="line1">KEYSTONE</span><br><span class="line2">ACADEMY</span></h1>
<p class="txt contact cover-address">4820 Palmetto Grove Road<br>Lake Orrin, Florida 33470</p>
<p class="txt contact cover-phone">(555) 014-2290<br>www.ashcombeprep.org</p>
</section>

<section class="spread spread--inside">
<svg class="art" viewBox="0 0 792 560" xmlns="http://www.w3.org/2000/svg">
  <defs>
    <linearGradient id="photoBand" x1="0" y1="0" x2="1" y2="0">
      <stop offset="0" stop-color="#dcb89a"/><stop offset=".35" stop-color="#b7c7a2"/><stop offset=".6" stop-color="#e6ddd4"/><stop offset="1" stop-color="#d6bca6"/>
    </linearGradient>
    <linearGradient id="fadeSky2" x1="0" y1="0" x2="0" y2="1">
      <stop offset="0" stop-color="#c3dcf3"/><stop offset="1" stop-color="#ffffff"/>
    </linearGradient>
    <linearGradient id="photoGroup" x1="0" y1="0" x2="0" y2="1">
      <stop offset="0" stop-color="#f3ece4"/><stop offset="1" stop-color="#d9c3ab"/>
    </linearGradient>
  </defs>
  <path role="img" aria-label="Photos: students learning with teachers in class" d="M0 0H792V175Q600 90 380 110Q150 130 0 190Z" fill="url(#photoBand)"/>
  <path d="M0 190Q150 130 380 110L380 119Q160 140 0 212Z" fill="var(--orange)"/>
  <path d="M380 110Q600 90 792 175V198Q600 112 380 119Z" fill="var(--blue)"/>
  <path d="M0 212Q160 140 380 119Q600 112 792 198V390H0Z" fill="url(#fadeSky2)"/>
  <line x1="264" y1="0" x2="264" y2="500" stroke="#000" stroke-opacity=".04"/>
  <line x1="528" y1="0" x2="528" y2="500" stroke="#000" stroke-opacity=".04"/>
  <rect role="img" aria-label="Photo: row of smiling students holding books and folders" x="400" y="340" width="370" height="160" fill="url(#photoGroup)"/>
  <line x1="25" y1="448" x2="380" y2="448" stroke="#bbbbbb" stroke-dasharray="2 2"/>
  <ellipse cx="65" cy="474" rx="38" ry="15" fill="none" stroke="var(--blue)" stroke-width="2.5"/>
  <rect x="150" y="464" width="100" height="20" fill="#6d8a6b"/>
  <rect x="290" y="462" width="95" height="22" fill="#b88a3c"/>
  <rect x="0" y="500" width="792" height="60" fill="var(--orange)"/>
  <path d="M294 518a4 4 0 0 1 8 0c0 3-4 7-4 7s-4-4-4-7z" fill="var(--blue)"/>
  <circle cx="298" cy="518" r="1.4" fill="#fff"/>
  <circle cx="578" cy="520" r="4.5" fill="var(--blue)"/>
  <path d="M576 518l1 -1 1 2 -.7.7a3 3 0 0 0 1.5 1.5l.7-.7 2 1-1 1a4 4 0 0 1-4.5-4.5z" fill="#fff"/>
  <circle cx="578" cy="534" r="4.5" fill="var(--blue)"/>
  <circle cx="578" cy="534" r="2.4" fill="none" stroke="#fff" stroke-width=".7"/>
  <line x1="575.6" y1="534" x2="580.4" y2="534" stroke="#fff" stroke-width=".6"/>
</svg>

<h2 class="txt diff-title">THE KEYSTONE<br>DIFFERENCE</h2>
<div class="txt col col-1">
  <p>The Ashcombe Keystone Academy is a specialized program offered at the Ashcombe Preparatory School. The 1:1 Academy provides middle and high school students an alternative to traditional education.</p>
  <p>Students are paired with a teacher to allow them to take courses individually, on their own schedule.</p>
</div>
<p class="txt col col-2">Our expert faculty can either accelerate or review educational content, allowing students to move at their own pace. Families can schedule classes around their own individual needs, making the 1:1 Academy a perfect option for today's specialized students.</p>
<p class="txt col col-3">Students are able to take part-time or full-time classes, and can start anytime throughout the school year. Students can also customize their schedule to start anytime during the day or create a schedule that only meets on certain days.</p>

<p class="txt footer-text foot-name">The Ashcombe Keystone Academy</p>
<p class="txt footer-text foot-address">4820 Palmetto Grove Road<br>Lake Orrin, FL 33470</p>
<p class="txt footer-text foot-contact">(555) 014-2290<br>www.ashcombeprep.org</p>
</section>

</body>
</html>
```